Brightwell Systems, a software development company, needs a website

We need a website to promote our software development company. The company is brand new and we want to market ourselves. We develop all kinds of software from web applications, to desktop applications, to mobile applications. Small company, not a lot of history, just need something flashy.

```html
<!DOCTYPE html>
<html lang="en">
<head>
<meta charset="utf-8">
<title>Brightwell Systems</title>
<link rel="stylesheet" href="https://fonts.googleapis.com/css2?family=Montserrat:wght@500;600;700;800&family=Open+Sans:wght@400;600&display=swap">
<style>
  :root {
    --blue: #2a7ae4;
    --navy: #0c1a33;
    --ink: #111418;
    --text: #4a4f57;
    --muted: #8a9099;
    --soft: #f6f6f7;
    --line: #e6e8eb;
    --white: #ffffff;
  }
  * { box-sizing: border-box; margin: 0; padding: 0; }
  html, body { width: 1200px; height: 3696px; overflow: hidden; }
  body { font-family: "Open Sans", Arial, sans-serif; color: var(--text); background: var(--white); }
  .wrap { width: 1020px; margin: 0 auto; position: relative; }
  .brand { font-family: "Montserrat", Arial, sans-serif; font-weight: 800; font-size: 19px; letter-spacing: .5px; color: var(--ink); text-transform: uppercase; }
  .brand .accent { color: var(--blue); }
  h2.section-title { font-family: "Montserrat", Arial, sans-serif; font-weight: 800; font-size: 26px; color: var(--ink); text-transform: uppercase; letter-spacing: .5px; }
  h2.section-title span { color: var(--blue); }
  .lead { font-size: 14px; line-height: 1.75; margin-top: 22px; color: var(--text); }

  /* Navigation */
  .site-nav { height: 76px; background: var(--white); box-shadow: 0 2px 10px rgba(0,0,0,.05); position: relative; z-index: 2; }
  .site-nav .wrap { display: flex; align-items: center; justify-content: space-between; height: 76px; }
  .nav-links { display: flex; gap: 48px; list-style: none; font-family: "Montserrat", Arial, sans-serif; font-weight: 600; font-size: 14px; color: var(--ink); }
  .nav-links li { position: relative; padding: 26px 0; }
  .nav-links li.active { color: var(--blue); }
  .nav-links li.active::after { content: ""; position: absolute; left: -6px; right: -6px; bottom: 0; height: 3px; background: var(--blue); }

  /* Hero */
  .hero { height: 614px; background: var(--soft); }
  .hero .wrap { height: 614px; }
  .hero-copy { position: absolute; left: 0; top: 176px; width: 520px; }
  .hero-copy h1 { font-family: "Montserrat", Arial, sans-serif; font-weight: 800; font-size: 26px; line-height: 1.4; color: var(--ink); text-transform: uppercase; white-space: nowrap; }
  .hero-copy h1 span { color: var(--blue); }
  .hero-copy p { font-size: 13px; line-height: 1.75; margin-top: 20px; width: 360px; }
  .hero-actions { display: flex; gap: 14px; margin-top: 34px; }
  .btn { display: inline-flex; align-items: center; justify-content: center; height: 50px; padding: 0 32px; font-family: "Montserrat", Arial, sans-serif; font-weight: 700; font-size: 13px; text-transform: uppercase; letter-spacing: .5px; }
  .btn-dark { background: var(--navy); color: var(--white); }
  .btn-outline { background: var(--white); color: var(--ink); border: 1px solid #cfd3d8; }
  .hero-illustration { position: absolute; left: 510px; top: 120px; width: 500px; height: 440px; border-radius: 14px; background: linear-gradient(135deg, #d9e6f9 0%, #b9cdec 55%, #a9b3c6 100%); }

  /* Services */
  .services { height: 660px; padding-top: 112px; }
  .service-grid { display: flex; gap: 18px; margin-top: 46px; }
  .service-card { width: 243px; height: 250px; background: var(--white); box-shadow: 0 4px 22px rgba(0,0,0,.08); display: flex; flex-direction: column; align-items: center; padding-top: 44px; }
  .service-art { width: 130px; height: 100px; border-radius: 6px; background: linear-gradient(135deg, #dbe8fb, #8fb8f2); }
  .service-card h3 { font-family: "Montserrat", Arial, sans-serif; font-weight: 700; font-size: 13px; color: var(--ink); text-transform: uppercase; margin-top: 44px; }

  /* Team */
  .team { height: 680px; background: var(--soft); padding-top: 100px; }
  .team-grid { display: flex; gap: 6px; margin-top: 46px; }
  .member { width: 336px; height: 338px; position: relative; overflow: hidden; }
  .member-photo { position: absolute; inset: 0; }
  .photo-1 { background: linear-gradient(160deg, #5b6b74, #2c3a44 70%); }
  .photo-2 { background: linear-gradient(120deg, #c78a5a, #3f3a38 55%, #d8b07a); }
  .photo-3 { background: linear-gradient(180deg, #e4e5e4, #b8bcbc 60%, #3d4a36); }
  .member-overlay { position: absolute; inset: 0; background: rgba(12,26,51,.55); padding: 104px 0 0 20px; color: var(--white); }
  .member-overlay h3 { font-family: "Montserrat", Arial, sans-serif; font-weight: 700; font-size: 26px; text-transform: uppercase; }
  .member-overlay p { font-size: 11px; text-transform: uppercase; letter-spacing: .5px; margin-top: 6px; }
  .member-social { display: flex; gap: 20px; margin-top: 28px; }
  .dot { width: 34px; height: 34px; border-radius: 50%; background: var(--blue); display: block; }

  /* Projects */
  .projects { height: 1075px; padding-top: 112px; }
  .project-tabs { display: flex; justify-content: center; gap: 52px; margin-top: 42px; list-style: none; font-family: "Montserrat", Arial, sans-serif; font-weight: 600; font-size: 14px; color: var(--ink); }
  .project-tabs li { padding-bottom: 16px; position: relative; }
  .project-tabs li.active { color: var(--blue); }
  .project-tabs li.active::after { content: ""; position: absolute; left: -4px; right: -4px; bottom: 0; height: 3px; background: var(--blue); }
  .project-grid { display: grid; grid-template-columns: 505px 505px; gap: 10px; margin-top: 40px; }
  .project { height: 270px; }
  .project-1 { background: radial-gradient(circle at 30% 40%, #6fb0ff, #1d55c9 45%, #0c2f8a); }
  .project-2 { background: linear-gradient(200deg, #c9dfea, #e9eff2 40%, #9aa3aa 75%, #5b6166); }
  .project-3 { background: linear-gradient(120deg, #e04b3a, #f3a23b 30%, #49b86a 55%, #3578d8 80%, #8a3fc2); }
  .project-4 { background: linear-gradient(160deg, #c9d6db, #6d8c95 50%, #2e4048); }
  .project-more { display: flex; justify-content: center; margin-top: 40px; }
  .project-more .btn { height: 48px; padding: 0 44px; }

  /* Newsletter */
  .newsletter { height: 196px; background: var(--navy); color: var(--white); }
  .newsletter .wrap { display: flex; justify-content: space-between; align-items: center; height: 196px; }
  .newsletter h2 { font-family: "Montserrat", Arial, sans-serif; font-weight: 800; font-size: 24px; text-transform: uppercase; }
  .newsletter h2 span { color: var(--blue); }
  .newsletter p { font-size: 13px; line-height: 1.6; margin-top: 12px; width: 320px; color: #dfe4ec; }
  .signup { width: 420px; height: 56px; border: 1px solid rgba(255,255,255,.6); display: flex; align-items: center; justify-content: space-between; padding: 0 10px 0 14px; font-size: 14px; color: var(--white); }
  .signup-btn { width: 34px; height: 34px; border-radius: 50%; background: var(--white); display: flex; align-items: center; justify-content: center; }

  /* Footer */
  .site-footer { height: 341px; }
  .site-footer .wrap { display: flex; height: 341px; align-items: flex-start; padding-top: 72px; }
  .footer-brand { width: 340px; padding-top: 68px; }
  .footer-col h4 { font-family: "Montserrat", Arial, sans-serif; font-weight: 700; font-size: 15px; color: var(--ink); text-transform: uppercase; }
  .footer-contact { width: 440px; }
  .contact-list { list-style: none; margin-top: 24px; font-size: 13px; }
  .contact-list li { display: flex; align-items: center; gap: 14px; margin-bottom: 20px; }
  .footer-social .social-row { display: flex; gap: 18px; margin-top: 30px; }
  .bottom-bar { height: 56px; background: var(--navy); color: var(--white); font-size: 13px; display: flex; align-items: center; justify-content: center; font-weight: 600; }
</style>
</head>
<body>

<header class="site-nav">
  <div class="wrap">
    <div class="brand">Brightwell <span class="accent">Systems</span></div>
    <ul class="nav-links">
      <li class="active">Home</li>
      <li>Services</li>
      <li>Team</li>
      <li>Work</li>
      <li>Contact</li>
    </ul>
  </div>
</header>

<section class="hero">
  <div class="wrap">
    <div class="hero-copy">
      <h1>We help you build a greater,<br>better <span>future.</span></h1>
      <p>We design and build dependable software for growing teams, turning bold ideas into fast, polished products that people enjoy using every day.</p>
      <div class="hero-actions">
        <span class="btn btn-dark">Contact us</span>
        <span class="btn btn-outline">Learn more</span>
      </div>
    </div>
    <div class="hero-illustration" role="img" aria-label="Illustration of a developer standing beside a large code window on a blue shape"></div>
  </div>
</section>

<section class="services">
  <div class="wrap">
    <h2 class="section-title">Our <span>Services</span></h2>
    <p class="lead">From first sketch to final launch, our small team plans, designs and ships software that fits your goals. We work closely with you at every step, keep things simple and deliver on time.</p>
    <p class="lead">Whatever platform you need, we bring clean code, careful testing and honest advice.</p>
    <div class="service-grid">
      <div class="service-card"><div class="service-art" role="img" aria-label="Illustration of browser windows"></div><h3>Website Development</h3></div>
      <div class="service-card"><div class="service-art" role="img" aria-label="Illustration of a smartphone app"></div><h3>Mobile Development</h3></div>
      <div class="service-card"><div class="service-art" role="img" aria-label="Illustration of a software dashboard"></div><h3>Software Development</h3></div>
      <div class="service-card"><div class="service-art" role="img" aria-label="Illustration of a user flow diagram"></div><h3>UI &amp; UX</h3></div>
    </div>
  </div>
</section>

<section class="team">
  <div class="wrap">
    <h2 class="section-title">Our <span>Team</span></h2>
    <p class="lead">Meet the people behind the work. We are a compact group of engineers and designers who care about quality, clear communication and software that lasts.</p>
    <div class="team-grid">
      <div class="member">
        <div class="member-photo photo-1" role="img" aria-label="Portrait photo of a team member"></div>
        <div class="member-overlay">
          <h3>Owen Hale</h3>
          <p>Founder / Architect</p>
          <div class="member-social">
            <span class="dot" aria-label="Social profile"></span>
            <span class="dot" aria-label="Social profile"></span>
            <span class="dot" aria-label="Social profile"></span>
          </div>
        </div>
      </div>
      <div class="member"><div class="member-photo photo-2" role="img" aria-label="Portrait photo of a team member in an office"></div></div>
      <div class="member"><div class="member-photo photo-3" role="img" aria-label="Portrait photo of a team member against a light wall"></div></div>
    </div>
  </div>
</section>

<section class="projects">
  <div class="wrap">
    <h2 class="section-title">Latest <span>Projects</span></h2>
    <p class="lead">A selection of recent work across web, mobile and desktop. Each project started with a clear problem and ended with software our clients rely on.</p>
    <ul class="project-tabs">
      <li class="active">Website</li>
      <li>Mobile</li>
      <li>Software</li>
    </ul>
    <div class="project-grid">
      <div class="project project-1" role="img" aria-label="Abstract blue fluid artwork"></div>
      <div class="project project-2" role="img" aria-label="Modern building facade against the sky"></div>
      <div class="project project-3" role="img" aria-label="Colourful abstract texture"></div>
      <div class="project project-4" role="img" aria-label="Glass skyscraper viewed from below"></div>
    </div>
    <div class="project-more"><span class="btn btn-dark">View all</span></div>
  </div>
</section>

<section class="newsletter">
  <div class="wrap">
    <div>
      <h2>Stay updated on <span>latest updates</span></h2>
      <p>Subscribe to our newsletter for the latest news and updates about our new products, services &amp; other stuff.</p>
    </div>
    <div class="signup">
      <span>Enter your email</span>
      <span class="signup-btn">
        <svg width="14" height="14" viewBox="0 0 14 14"><path d="M2 7h9M7 3l4 4-4 4" stroke="#0c1a33" stroke-width="2" fill="none"/></svg>
      </span>
    </div>
  </div>
</section>

<footer class="site-footer">
  <div class="wrap">
    <div class="footer-brand"><div class="brand">Brightwell <span class="accent">Systems</span></div></div>
    <div class="footer-col footer-contact">
      <h4>Contact</h4>
      <ul class="contact-list">
        <li><svg width="16" height="16" viewBox="0 0 16 16"><path d="M4 1l3 3-2 2c1 2 3 4 5 5l2-2 3 3-2 3C7 14 2 9 1 4z" fill="#2a7ae4"/></svg>(+1) 555 014 2288</li>
        <li><svg width="16" height="16" viewBox="0 0 16 16"><path d="M8 1a5 5 0 0 1 5 5c0 4-5 9-5 9S3 10 3 6a5 5 0 0 1 5-5z" fill="#2a7ae4"/><circle cx="8" cy="6" r="2" fill="#fff"/></svg>42 Orchard Lane, Millbrook, PA 17002</li>
        <li><svg width="16" height="16" viewBox="0 0 16 16"><rect x="1" y="3" width="14" height="10" fill="none" stroke="#2a7ae4" stroke-width="1.6"/><path d="M1 3l7 6 7-6" fill="none" stroke="#2a7ae4" stroke-width="1.6"/></svg>hello@brightwellsystems.com</li>
      </ul>
    </div>
    <div class="footer-col footer-social">
      <h4>Social links</h4>
      <div class="social-row">
        <span class="dot" aria-label="Social profile"></span>
        <span class="dot" aria-label="Social profile"></span>
        <span class="dot" aria-label="Social profile"></span>
      </div>
    </div>
  </div>
</footer>

<div class="bottom-bar">All rights reserved. &copy; 2019</div>

</body>
</html>
```